VFX Company Business Card Design Project

The Ember Vale is a decentralized Visual Effects Studio servicing the television and feature film industries.
Project Brief:
Take our logo that was previously designed on Pixel Harbor and make a double sided business card.
Requirements:
- Card MUST be double sided.
- Front of card MUST have the yellow part of our logo against the dark grey background.
- Back of card is completely up to the designer.
- Back of card must include the complete company logo.
Please follow these File Preparation guidelines:
http://printmoor.example/infopage?file=filetype_en&s=PrintMoor_new&lang=en
Industry/Entity Type
Business
Look and feel
Each slider illustrates characteristics of the customer's brand and the style your logo design should communicate.

```html
<!DOCTYPE html>
<html lang="en">
<head>
<meta charset="utf-8">
<title>The Ember Vale – Business Card</title>
<link href="https://fonts.googleapis.com/css2?family=Didact+Gothic&display=swap" rel="stylesheet">
<style>
  :root {
    --backdrop: #8c8a8d;
    --card: #2a2a2b;
    --card-edge: #1d1d1e;
    --accent: #fcc72b;
    --text: #f4f4f4;
    --logo-grey: #9aa1a3;
  }
  * { box-sizing: border-box; margin: 0; padding: 0; }
  html, body { width: 1200px; height: 960px; overflow: hidden; }
  body {
    background: var(--backdrop);
    font-family: "Didact Gothic", "Century Gothic", sans-serif;
    color: var(--text);
    position: relative;
  }
  .card {
    position: absolute;
    left: 250px;
    width: 700px;
    height: 400px;
    background: var(--card);
    border: 1px solid var(--card-edge);
    box-shadow: 0 10px 28px rgba(0,0,0,0.35);
  }
  .card--info { top: 60px; }
  .card--front { top: 500px; }

  .brand {
    position: absolute;
    top: 58px;
    right: 56px;
    display: flex;
    align-items: center;
    gap: 16px;
  }
  .brand__dot {
    width: 34px; height: 34px;
    border-radius: 50%;
    background: var(--accent);
  }
  .brand__name {
    font-size: 34px;
    letter-spacing: 1px;
    color: var(--logo-grey);
    text-transform: uppercase;
  }

  .person { position: absolute; left: 68px; top: 222px; }
  .person__name { font-size: 32px; font-weight: 400; letter-spacing: 0.3px; }
  .person__role { font-size: 17px; margin-top: 2px; }

  .contact { position: absolute; left: 68px; top: 296px; list-style: none; }
  .contact__item {
    display: flex; align-items: center; gap: 12px;
    font-size: 16px; line-height: 23px;
  }
  .contact__icon { width: 15px; height: 15px; flex: none; }

  .front-mark {
    position: absolute;
    inset: 0;
    display: flex;
    align-items: center;
    justify-content: center;
    gap: 22px;
  }
  .front-mark__dot {
    width: 58px; height: 58px;
    border-radius: 50%;
    background: var(--accent);
  }
  .front-mark__name {
    font-size: 52px;
    color: var(--accent);
    text-transform: uppercase;
    letter-spacing: 2px;
  }
</style>
</head>
<body>
  <section class="card card--info" aria-label="Business card, contact side">
    <div class="brand">
      <span class="brand__dot"></span>
      <span class="brand__name">The Ember Vale</span>
    </div>

    <div class="person">
      <h1 class="person__name">Marcus Hale</h1>
      <p class="person__role">President</p>
    </div>

    <ul class="contact">
      <li class="contact__item">
        <svg class="contact__icon" viewBox="0 0 16 16" aria-hidden="true"><path fill="#fcc72b" d="M8 0a5.5 5.5 0 0 0-5.5 5.5C2.5 10 8 16 8 16s5.5-6 5.5-10.5A5.5 5.5 0 0 0 8 0zm0 8a2.5 2.5 0 1 1 0-5 2.5 2.5 0 0 1 0 5z"/></svg>
        P.O Box 4100, Quay Point AU 3QX
      </li>
      <li class="contact__item">
        <svg class="contact__icon" viewBox="0 0 16 16" aria-hidden="true"><path fill="#fcc72b" d="M3.6 1 6 4.2 4.6 6a9 9 0 0 0 5.4 5.4L11.8 10 15 12.4 13.6 15C6.8 15 1 9.2 1 2.4z"/></svg>
        +01 555 01842
      </li>
      <li class="contact__item">
        <svg class="contact__icon" viewBox="0 0 16 16" aria-hidden="true"><path fill="#fcc72b" d="M0 3h16v1.2L8 9 0 4.2zm0 2.6 8 4.8 8-4.8V13H0z"/></svg>
        info@embervale.example
      </li>
      <li class="contact__item">
        <svg class="contact__icon" viewBox="0 0 16 16" aria-hidden="true"><g fill="none" stroke="#fcc72b" stroke-width="2"><rect x="1.5" y="8" width="7" height="4" rx="2" transform="rotate(-35 5 10)"/><rect x="7.5" y="4" width="7" height="4" rx="2" transform="rotate(-35 11 6)"/></g></svg>
        www.embervale.example
      </li>
    </ul>
  </section>

  <section class="card card--front" aria-label="Business card, brand side">
    <div class="front-mark">
      <span class="front-mark__dot"></span>
      <span class="front-mark__name">The Ember Vale</span>
    </div>
  </section>
</body>
</html>
```